Small, static, 2 page website that promotes 3-6 workshops

This is a microsite for my company that promotes 3 (and later 6) security workshops for developers. The address is going to be vakwerk-leerlijnen.nl so it is very important that the title reads 'Vakwerk Leerlijnen' and the subtitle reads 'voor ontwikkelaars' (means for developers in dutch).

On the frontpage, there will be a small introduction text (about 50 words) about the workshops in general and there should be 3 workshops listed on the frontpage with also a small introduction text. All the workshops are cyber security/hacking related so maybe a small graphic for every workshop would lighten things up.

Then when a visitor clicks a 'more info' button a detail page about that specific workshop with a longer description, a date/location, a 'book now' button and a price should be show.

I have include a quick drawing of what I have in mind for the frontpage, this is not set in stone so you could come up with something else.

I also included my company logo, it should be clear on the site that these workshops are 'Brightmoor Labs' workshops.

Target Market(s)

Development companies looking for security workshops, the responsible people for those type of workshops are usually security officers, lead developers/managers or developers themselves.

Industry/Entity Type

It Company

Number of Pages Required

2 page

Font styles to use
Sans Serif
Other font styles liked:
• Please choose a font you

Requirements
Must have
• 3 highlighted trainings on the frontpage and a detail page and the title and subtitle as headings on the page.
Nice to have
• I'd really like to have the 3 boxes on the frontpage to have icons or some sort of images. The first 3 workshops that are going to be on the page are:
• - Security awareness for developers
• - Web application security from a hackers perspective
• - Penetrationtesting for developers

```html
<!DOCTYPE html>
<html lang="en">
<head>
<meta charset="utf-8">
<title>Brightmoor Labs – Vakwerk Leerlijnen</title>
<link href="https://fonts.googleapis.com/css2?family=Open+Sans:wght@400;600;700;800&display=swap" rel="stylesheet">
<style>
:root{
  --navy:#173a63;
  --navy-dark:#12304f;
  --text:#5a5a5a;
  --light:#f2f2f2;
  --white:#ffffff;
  --footer:#7d7d7d;
  --arrow:#b5b5b5;
}
*{box-sizing:border-box;margin:0;padding:0}
html,body{width:758px;height:1200px;overflow:hidden}
body{font-family:"Open Sans",sans-serif;color:var(--text);background:var(--white);position:relative}

.hero{position:absolute;left:0;top:0;width:758px;height:370px;overflow:hidden}
.hero-photo{position:absolute;inset:0;background:linear-gradient(180deg,#8b8f96 0%,#9a9c9f 30%,#7a6a66 60%,#5c5a5e 100%)}
.hero-photo::after{content:"";position:absolute;inset:0;background:radial-gradient(ellipse at 50% 60%,rgba(170,60,55,.35),transparent 70%)}
.brand{position:absolute;left:47px;top:24px;display:flex;align-items:center;gap:8px;color:var(--white);font-weight:600;font-size:19px;letter-spacing:1px;text-transform:uppercase}
.brand-mark{width:22px;height:22px;border-radius:50%;background:var(--white)}
.nav{position:absolute;top:29px;left:346px;display:flex;align-items:center}
.nav a{color:var(--white);text-decoration:none;font-size:8.5px;font-weight:700;text-transform:uppercase;padding:0 13px;line-height:22px}
.nav a.active{background:var(--navy);margin-right:0}
.hero-title{position:absolute;left:0;right:0;top:150px;text-align:center;color:var(--white);font-weight:800;font-size:43px;line-height:39px;text-transform:uppercase;text-shadow:0 2px 4px rgba(0,0,0,.35);letter-spacing:.5px}
.dots{position:absolute;left:0;right:0;display:flex;justify-content:center;gap:5px}
.dots span{width:8px;height:8px;border-radius:50%;background:#1b1b1b}
.hero .dots{top:342px}
.hero .dots span:first-child{background:var(--white)}

.welcome{position:absolute;top:370px;left:0;width:758px;height:216px;text-align:center}
.section-title{color:var(--navy);font-weight:700;font-size:17px;text-transform:uppercase;letter-spacing:.3px}
.welcome .section-title{margin-top:40px}
.welcome p{font-size:10px;line-height:17px;margin:10px auto 0;width:650px}
.btn{display:inline-block;background:var(--navy);color:var(--white);text-decoration:none;font-weight:700;text-transform:uppercase;border-bottom:2px solid var(--navy-dark)}
.btn-lg{margin-top:17px;width:114px;height:30px;line-height:30px;font-size:10px}

.workshops{position:absolute;top:586px;left:0;width:758px;height:398px;background:var(--light);text-align:center}
.workshops .section-title{margin-top:29px}
.cards{position:absolute;top:61px;left:47px;display:flex;gap:18px}
.card{width:209px;height:287px;background:var(--white);border-bottom:2px solid #dcdcdc;position:relative}
.card svg{position:absolute;left:50%;transform:translateX(-50%);top:28px}
.card h3{position:absolute;top:109px;left:10px;right:10px;color:var(--navy);font-size:11.5px;font-weight:700;line-height:17px;text-transform:uppercase;letter-spacing:.3px}
.card p{position:absolute;left:15px;right:15px;font-size:10px;line-height:15.3px}
.card .btn{position:absolute;top:236px;left:60px;width:89px;height:26px;line-height:25px;font-size:8.5px}
.slide-arrow{position:absolute;top:171px}
.workshops .dots{top:369px}
.workshops .dots span{background:#2b3b4d}

.contact{position:absolute;top:984px;left:0;width:758px;height:73px;display:flex;justify-content:center;align-items:center;gap:16px}
.contact-item{display:flex;align-items:center;gap:9px;color:var(--navy);font-size:10px;font-weight:600}
.contact-icon{width:28px;height:28px;border:2px solid var(--navy);border-radius:50%;display:flex;align-items:center;justify-content:center}

.footer{position:absolute;top:1057px;left:0;width:758px;height:143px;background:var(--footer);text-align:center;color:var(--white)}
.footer .brand{position:static;justify-content:center;margin-top:30px;font-size:15px}
.footer .brand-mark{width:16px;height:16px}
.copyright{font-size:8.5px;margin-top:21px}
.social{display:flex;justify-content:center;gap:8px;margin-top:10px}
.social span{width:14px;height:14px;border-radius:2px;background:var(--white)}
</style>
</head>
<body>

<header class="hero">
  <div class="hero-photo" role="img" aria-label="Photo of developers attending a security training in a classroom with laptops"></div>
  <div class="brand"><span class="brand-mark"></span>Brightmoor Labs</div>
  <nav class="nav">
    <a class="active" href="#">Home</a>
    <a href="#">About us</a>
    <a href="#">Workshops</a>
    <a href="#">Why choose us?</a>
    <a href="#">Contact us</a>
  </nav>
  <h1 class="hero-title">Vakwerk Leerlijnen<br>voor ontwikkelaars</h1>
  <div class="dots"><span></span><span></span><span></span><span></span></div>
</header>

<section class="welcome">
  <h2 class="section-title">Welcome to Brightmoor Labs</h2>
  <p>From the first moment you have your own cybersecurity expert who can advise his knowledge and years of experience in the right way on the steps to take to achieve the desired level of security within your organization. So you sit flush with the right person at the table and have already benefited from the first call.</p>
  <a class="btn btn-lg" href="#">Read more</a>
</section>

<section class="workshops">
  <h2 class="section-title">Workshops</h2>

  <svg class="slide-arrow" style="left:28px" width="10" height="18" viewBox="0 0 10 18"><path d="M8 2 2 9l6 7" fill="none" stroke="var(--arrow)" stroke-width="2.5"/></svg>
  <svg class="slide-arrow" style="left:720px" width="10" height="18" viewBox="0 0 10 18"><path d="M2 2l6 7-6 7" fill="none" stroke="var(--arrow)" stroke-width="2.5"/></svg>

  <div class="cards">
    <article class="card">
      <svg width="62" height="56" viewBox="0 0 62 56">
        <g fill="#707070">
          <circle cx="22" cy="28" r="15"/>
          <g stroke="#707070" stroke-width="7">
            <path d="M22 8v40M2 28h40M8 14l28 28M36 14 8 42"/>
          </g>
          <circle cx="48" cy="12" r="8"/>
          <g stroke="#707070" stroke-width="4"><path d="M48 1v22M37 12h22M40 4l16 16M56 4 40 20"/></g>
          <circle cx="48" cy="44" r="8"/>
          <g stroke="#707070" stroke-width="4"><path d="M48 33v22M37 44h22M40 36l16 16M56 36 40 52"/></g>
        </g>
        <g fill="#fff"><circle cx="22" cy="28" r="6"/><circle cx="48" cy="12" r="3"/><circle cx="48" cy="44" r="3"/></g>
      </svg>
      <h3>Security awareness<br>for developers</h3>
      <p style="top:147px">By vulnerabilities to execute scan you get a low price insight into the current vulnerabilities in your network or application.</p>
      <a class="btn" href="#">More info</a>
    </article>

    <article class="card">
      <svg width="64" height="60" viewBox="0 0 64 60">
        <rect x="2" y="2" width="46" height="56" fill="#707070"/>
        <g stroke="#fff" stroke-width="2"><path d="M8 14h24M8 20h32M8 26h32M8 32h32M8 38h32M8 44h24"/></g>
        <path d="M58 4l4 4-24 30-7 3 2-7z" fill="#707070" stroke="#fff" stroke-width="1.5"/>
      </svg>
      <h3>Web application<br>security from a hackers<br>perspective</h3>
      <p style="top:164px">By vulnerabilities to execute scan you get a low price insight into the current vulnerabilities in your network or application.</p>
      <a class="btn" href="#">More info</a>
    </article>

    <article class="card">
      <svg width="64" height="60" viewBox="0 0 64 60">
        <rect x="3" y="1" width="32" height="57" rx="4" fill="#707070"/>
        <rect x="6" y="8" width="26" height="42" fill="#f4f4f4"/>
        <circle cx="28" cy="29" r="12" fill="#fff" stroke="#707070" stroke-width="4"/>
        <path d="M37 38l16 13" stroke="#707070" stroke-width="6" stroke-linecap="round"/>
      </svg>
      <h3>Penetrationtesting<br>for developers</h3>
      <p style="top:147px">By vulnerabilities to execute scan you get a low price insight into the current vulnerabilities in your network or application.</p>
      <a class="btn" href="#">More info</a>
    </article>
  </div>

  <div class="dots"><span></span><span></span></div>
</section>

<section class="contact">
  <div class="contact-item">
    <span class="contact-icon"><svg width="11" height="8" viewBox="0 0 11 8"><rect width="11" height="8" rx="1" fill="var(--navy)"/><path d="M0.5 0.8 5.5 4.5l5-3.7" fill="none" stroke="#fff" stroke-width="1"/></svg></span>
    info@brightmoorlabs.nl
  </div>
  <div class="contact-item">
    <span class="contact-icon"><svg width="8" height="11" viewBox="0 0 8 11"><path d="M4 0a4 4 0 0 1 4 4c0 3-4 7-4 7S0 7 0 4a4 4 0 0 1 4-4z" fill="var(--navy)"/><circle cx="4" cy="4" r="1.5" fill="#fff"/></svg></span>
    Rotterdam
  </div>
  <div class="contact-item">
    <span class="contact-icon"><svg width="10" height="10" viewBox="0 0 10 10"><path d="M2 0l2 2.5-1.2 1.3a6 6 0 0 0 3.4 3.4L7.5 6 10 8 8.5 10C4 10 0 6 0 1.5z" fill="var(--navy)"/></svg></span>
    010-5550142
  </div>
</section>

<footer class="footer">
  <div class="brand"><span class="brand-mark"></span>Brightmoor Labs</div>
  <p class="copyright">Copyright © 2016 - Brightmoor Labs. All Right Reserved</p>
  <div class="social"><span></span><span></span><span></span><span></span><span></span></div>
</footer>

</body>
</html>
```